K.T.L Services

We are needing business cards for a construction company that does everything from painting and detailing, maintenance, Sheetrock repairs, demolition, tile and wood floors. Also, K.T.L stands for Detailing, maintenance, and Painting. We would like the colors to be closer to the colors grey and light brown/khaki, but if there is any other suggestions that would go better with the design we are open to ideas.

Industry/Entity Type

Business

Contact Information for Business Card

Owner / Operator Owen Tallis (555) 412-3907 / (555) 738- 2164

Font styles to use
Sans Serif

```html
<!DOCTYPE html>
<html lang="en">
<head>
<meta charset="utf-8">
<title>K.T.L Services – Business Card</title>
<link rel="stylesheet" href="https://fonts.googleapis.com/css2?family=Lato:wght@400;700&family=Saira+Semi+Condensed:wght@400;600&display=swap">
<style>
  :root {
    --paper: #e5edef;
    --panel: #c7d7d9;
    --orange: #f7860f;
    --ink: #111111;
    --band: #0f0f0f;
    --white: #ffffff;
  }
  * { margin: 0; padding: 0; box-sizing: border-box; }
  html, body { width: 1200px; height: 702px; overflow: hidden; background: var(--paper); }
  .card {
    position: relative; width: 1200px; height: 702px; overflow: hidden;
    background: var(--paper);
    font-family: "Lato", sans-serif; color: var(--ink);
  }
  .shapes { position: absolute; inset: 0; }

  .brand {
    position: absolute; left: 641px; top: 77px; width: 478px; height: 109px;
    background: var(--panel); border-radius: 8px;
  }
  .brand-name {
    position: absolute; left: 30px; top: 22px;
    font-weight: 700; font-size: 56px; letter-spacing: 2px; line-height: 64px;
  }
  .brand-services {
    position: absolute; left: 251px; top: 10px; width: 216px; height: 88px;
    background: var(--orange); border-radius: 20px;
    padding: 4px 0 0 15px;
    font-size: 23px; line-height: 27px;
  }

  .contact-row {
    position: absolute; left: 641px; width: 478px;
    background: var(--panel); border-radius: 6px;
    display: flex; align-items: center;
  }
  .contact-icon {
    width: 79px; height: 100%; background: var(--orange);
    border-radius: 6px 0 0 6px; display: flex; align-items: center; justify-content: center;
  }
  .contact-text { padding-left: 26px; font-size: 31px; line-height: 36px; }
  .row-phone { top: 223px; height: 77px; }
  .row-web { top: 307px; height: 75px; }
  .row-address { top: 389px; height: 77px; }

  .owner { position: absolute; left: 101px; top: 430px; font-family: "Saira Semi Condensed", sans-serif; }
  .owner-name { font-weight: 600; font-size: 40px; letter-spacing: 1px; line-height: 44px; }
  .owner-title { font-size: 27px; line-height: 30px; letter-spacing: -0.5px; }

  .footer-item {
    position: absolute; top: 561px; display: flex; align-items: center; gap: 14px;
    color: var(--white); font-size: 30px; letter-spacing: 0.5px;
  }
  .footer-phone { left: 104px; }
  .footer-email { left: 473px; }
</style>
</head>
<body>
<main class="card">
  <svg class="shapes" width="1200" height="702" viewBox="0 0 1200 702" aria-hidden="true">
    <path d="M0 389 H434 Q446 389 456 399 L606 545 H0 Z" fill="var(--orange)"/>
    <rect x="0" y="545" width="1200" height="77" fill="var(--band)"/>
    <rect x="0" y="622" width="1200" height="80" fill="var(--orange)"/>
  </svg>

  <header class="brand">
    <div class="brand-name">K.T.L</div>
    <div class="brand-services">Detailing<br>Maintenance<br>Painting</div>
  </header>

  <div class="contact-row row-phone">
    <div class="contact-icon">
      <svg width="58" height="58" viewBox="0 0 58 58" fill="none" stroke="#fff" stroke-width="2.5">
        <circle cx="29" cy="29" r="26"/>
        <circle cx="29" cy="29" r="13"/>
        <circle cx="29" cy="29" r="5"/>
        <path d="M29 10v6M29 42v6M10 29h6M42 29h6M15.6 15.6l4.2 4.2M38.2 38.2l4.2 4.2M15.6 42.4l4.2-4.2M38.2 19.8l4.2-4.2"/>
      </svg>
    </div>
    <div class="contact-text">(555) 412-3907<br>(555) 738- 2164</div>
  </div>

  <div class="contact-row row-web">
    <div class="contact-icon">
      <svg width="58" height="58" viewBox="0 0 58 58" fill="none" stroke="#fff" stroke-width="2.5">
        <circle cx="29" cy="29" r="26"/>
        <circle cx="29" cy="29" r="11"/>
        <path d="M18 29h22M29 18v22"/>
      </svg>
    </div>
    <div class="contact-text">www.website.com</div>
  </div>

  <div class="contact-row row-address">
    <div class="contact-icon">
      <svg width="58" height="58" viewBox="0 0 58 58" fill="none" stroke="#fff" stroke-width="2.5">
        <circle cx="29" cy="29" r="26"/>
        <path d="M40 16L24 34M24 34l-5 8 8-5z" stroke-linejoin="round"/>
      </svg>
    </div>
    <div class="contact-text">0000 address<br>New York 00000</div>
  </div>

  <section class="owner">
    <div class="owner-name">OWEN TALLIS</div>
    <div class="owner-title">OWNER/OPERATOR</div>
  </section>

  <div class="footer-item footer-phone">
    <svg width="46" height="46" viewBox="0 0 46 46" aria-hidden="true">
      <circle cx="23" cy="23" r="21" fill="var(--white)"/>
      <rect x="16" y="10" width="14" height="25" rx="2.5" fill="none" stroke="var(--band)" stroke-width="2.5"/>
      <circle cx="23" cy="30.5" r="1.6" fill="var(--band)"/>
    </svg>
    <span>(555) 412-3907</span>
  </div>

  <div class="footer-item footer-email">
    <svg width="46" height="46" viewBox="0 0 46 46" aria-hidden="true">
      <circle cx="23" cy="23" r="21" fill="var(--white)"/>
      <rect x="11" y="15" width="24" height="16" rx="1.5" fill="var(--band)"/>
      <path d="M11.5 15.5L23 25l11.5-9.5" fill="none" stroke="var(--white)" stroke-width="2"/>
    </svg>
    <span>info@website.com</span>
  </div>
</main>
</body>
</html>
```